USB Flash Drive Catalogue

I would like to make a paper catalogue of the products from our Quorvel store. There are currently 209 items on Quorvel. Some would be excluded. The listings have pricing and would need to be organized a bit different but all the information is there.

https://www.quorvel.com/shop/BrightPinStock/items?ref=pagination&page=1

Store

```html
<!DOCTYPE html>
<html lang="en">
<head>
<meta charset="utf-8">
<title>BrightPinStock Catalogue – Contents and Company Profile</title>
<link rel="stylesheet" href="https://fonts.googleapis.com/css2?family=Ubuntu:wght@400;500;700&family=Open+Sans:wght@400;600&display=swap">
<style>
  :root {
    --backdrop: #d8d7d3;
    --paper: #f7f7f6;
    --orange: #d9822b;
    --charcoal: #3f4144;
    --ink: #2c2d2f;
    --rule: #4a4c4f;
    --white: #ffffff;
  }
  * { box-sizing: border-box; margin: 0; padding: 0; }
  html, body { width: 1200px; height: 804px; overflow: hidden; background: var(--backdrop); }
  .spread { position: absolute; left: 40px; top: 32px; width: 1120px; height: 740px; display: flex; box-shadow: 0 10px 30px rgba(0,0,0,.18); }
  .page { position: relative; width: 560px; height: 740px; background: var(--paper); overflow: hidden; }
  .page--left { background: linear-gradient(90deg, var(--paper) 85%, #e6e6e4 100%); }
  .page--right { background: linear-gradient(90deg, #e3e3e1 0%, var(--paper) 12%); }

  .header-rule { position: absolute; top: 44px; height: 2px; background: var(--rule); }
  .header-tab { position: absolute; top: 32px; }
  .brand { position: absolute; top: 28px; display: flex; align-items: center; gap: 6px; font-family: "Ubuntu", sans-serif; font-weight: 700; font-size: 13px; color: var(--orange); white-space: nowrap; }
  .brand__dot { width: 16px; height: 16px; border-radius: 50%; background: var(--charcoal); }

  .page-title { position: absolute; font-family: "Ubuntu", sans-serif; font-weight: 500; font-size: 34px; color: var(--charcoal); letter-spacing: -0.5px; }
  .page-title em { font-style: normal; color: var(--orange); }

  .toc { position: absolute; left: 110px; top: 316px; list-style: none; }
  .toc__item { display: flex; align-items: center; height: 27px; margin-bottom: 10px; }
  .toc__num { width: 44px; height: 27px; background: var(--charcoal); color: var(--white); font-family: "Ubuntu", sans-serif; font-weight: 700; font-size: 19px; display: flex; align-items: center; justify-content: center; border-radius: 3px 0 0 3px; }
  .toc__label { width: 300px; height: 24px; background: var(--orange); color: var(--white); font-family: "Ubuntu", sans-serif; font-size: 12px; display: flex; align-items: center; padding-left: 10px; border-radius: 0 4px 4px 0; }

  .profile { position: absolute; left: 70px; top: 250px; width: 430px; font-family: "Open Sans", sans-serif; font-size: 9.6px; line-height: 1.42; color: var(--ink); }
  .profile p { margin-bottom: 12px; }
  .profile .lead { margin-bottom: 6px; }

  .footer { position: absolute; bottom: 18px; height: 38px; display: flex; z-index: 1; }
  .footer__social { width: 140px; height: 38px; background: var(--orange); display: flex; align-items: center; justify-content: center; gap: 12px; }
  .footer__social span { width: 13px; height: 13px; border-radius: 2px; background: var(--white); opacity: .9; }
  .footer__band { height: 38px; background: var(--charcoal); display: flex; align-items: center; justify-content: center; font-family: "Open Sans", sans-serif; font-size: 9.5px; color: var(--white); }
  .page-num { position: absolute; bottom: 27px; z-index: 2; width: 20px; height: 20px; border-radius: 50%; background: var(--white); border: 2px solid var(--orange); font-family: "Ubuntu", sans-serif; font-weight: 700; font-size: 10px; color: var(--charcoal); display: flex; align-items: center; justify-content: center; }
</style>
</head>
<body>
<main class="spread">
  <section class="page page--left" aria-label="Page 2, table of contents">
    <svg class="header-tab" style="left:0" width="62" height="26" viewBox="0 0 62 26" aria-hidden="true">
      <rect x="0" y="2" width="30" height="22" fill="var(--orange)"/>
      <polygon points="30,2 56,2 48,24 22,24" fill="var(--charcoal)"/>
      <circle cx="39" cy="13" r="6" fill="var(--orange)"/>
      <polygon points="37,10 42,13 37,16" fill="var(--white)"/>
    </svg>
    <div class="header-rule" style="left:60px; width:345px;"></div>
    <div class="brand" style="left:414px;"><span class="brand__dot"></span>BrightPinStock</div>

    <h1 class="page-title" style="left:150px; top:220px;">Table of <em>Contents</em></h1>

    <ol class="toc">
      <li class="toc__item"><span class="toc__num">03</span><span class="toc__label">Company Profile</span></li>
      <li class="toc__item"><span class="toc__num">04</span><span class="toc__label">Custom USB Drives</span></li>
      <li class="toc__item"><span class="toc__num">05</span><span class="toc__label">Wooden USB Drives</span></li>
      <li class="toc__item"><span class="toc__num">06</span><span class="toc__label">USB in Paper Boxes</span></li>
      <li class="toc__item"><span class="toc__num">07</span><span class="toc__label">USB in Wooden Boxes</span></li>
      <li class="toc__item"><span class="toc__num">08</span><span class="toc__label">Unique USB Drives</span></li>
      <li class="toc__item"><span class="toc__num">09</span><span class="toc__label">Bulk Quantity</span></li>
      <li class="toc__item"><span class="toc__num">10</span><span class="toc__label">Customer Reviews</span></li>
    </ol>

    <footer class="footer" style="left:0;">
      <div class="footer__social" aria-label="Social links"><span></span><span></span><span></span><span></span></div>
      <div class="footer__band" style="width:414px; margin-left:6px;">info@yourwebsite.com | www.quorvel.com/shop/BrightPinStock</div>
    </footer>
    <div class="page-num" style="left:518px;">2</div>
  </section>

  <section class="page page--right" aria-label="Page 3, company profile">
    <div class="brand" style="left:36px;"><span class="brand__dot"></span>BrightPinStock</div>
    <div class="header-rule" style="left:160px; width:340px;"></div>
    <svg class="header-tab" style="right:0" width="62" height="26" viewBox="0 0 62 26" aria-hidden="true">
      <polygon points="14,2 40,2 32,24 6,24" fill="var(--charcoal)"/>
      <circle cx="23" cy="13" r="6" fill="var(--orange)"/>
      <polygon points="25,10 20,13 25,16" fill="var(--white)"/>
      <rect x="32" y="2" width="30" height="22" fill="var(--orange)"/>
    </svg>

    <h1 class="page-title" style="left:70px; top:190px;">Company <em>Profile</em></h1>

    <div class="profile">
      <p class="lead">A short word from our founders.</p>
      <p>We began as a small workshop with one goal: to ship custom flash drives the same day an order arrives. Since then we have grown into a busy studio that prints, engraves and packs thousands of drives each month for schools, agencies, photographers and event teams. Every drive is tested before it leaves our bench, and every logo proof is checked by a real person. We keep a wide range of shapes in stock, from slim metal cards to warm wooden blocks, so your idea can move from sketch to parcel quickly. Our team answers every message within one working day, and we are always glad to help.</p>
      <p>Our drives come in many capacities and finishes, and each one can carry your artwork in full colour or as a clean laser engraving. We can also preload files, set a custom volume name and lock content so it cannot be erased. Gift boxes in paper or wood complete the set and make each drive feel like a small present for clients, staff or guests.</p>
      <p>For large orders we offer tiered pricing, free design help and tracked shipping, so bulk runs stay simple from the first quote to the final delivery.</p>
      <p>Browse the pages that follow to see our full range, then send us a note with your quantity, deadline and artwork. We will reply with a proof and a clear price, usually on the very same day.</p>
    </div>

    <footer class="footer" style="right:0;">
      <div class="footer__band" style="width:414px; margin-right:6px;">info@hollowmere.com | www.quorvel.com/shop/BrightPinStock</div>
      <div class="footer__social" aria-label="Social links"><span></span><span></span><span></span><span></span></div>
    </footer>
    <div class="page-num" style="left:22px;">3</div>
  </section>
</main>
</body>
</html>
```